Piano teaching business needs a business card and logo design.

We provide piano lessons to children and adults. The card / logo should be colourful and playful and appeal to kids but retain a professional mature approach which also appeals to adults. I like the Colours orange and blue as dominating theme colours, but we are open to all colour ideas. The business name is: BLUE OWL SWING. We do not like typical black and white images of piano keyboards. A cartoon character of a jazz inspired orange coloured fat cat playing piano is one idea but we are open to all ideas.

Target Market(s)

Domestic, Local population, adults and children.

Industry/Entity Type

Service

Contact Information for Business Card

Piano teacher
Mel T Karsh
27 Wendover Close
Arundel
4214 QLD
T: 07 5283 9147
M: 0438 752 906
E: keyvale@mailbrook.net
www. keyvale.net.au

Logo Text

Blue Owl Swing

Font styles to use
Sans Serif

Colors
f78f20
f37122
0493ce
0455a3
fbed22

Requirements
Must have
• Colours.
Nice to have
• Cartoon style fat cat. Limited music notation.
Should not have
• Dominating images of keyboards.

```html
<!DOCTYPE html>
<html lang="en">
<head>
<meta charset="utf-8">
<title>Blue Owl Swing – Business Card</title>
<link rel="stylesheet" href="https://fonts.googleapis.com/css2?family=Arimo:wght@400;700&family=Merriweather:wght@900&display=swap">
<style>
  :root {
    --page: #e9e6e3;
    --card-dark: #14100d;
    --accent-orange: #f37122;
    --name-orange: #f78f20;
    --text-light: #ffffff;
    --disc-light: #f1f0ef;
    --disc-mid: #d9d6d4;
    --brand-blue: #0455a3;
  }
  * { margin: 0; padding: 0; box-sizing: border-box; }
  html, body { width: 1200px; height: 900px; overflow: hidden; }
  body { background: var(--page); position: relative; font-family: "Arimo", Arial, sans-serif; }

  .business-card {
    position: absolute; left: 100px; top: 141px;
    width: 1000px; height: 618px;
    background: var(--card-dark);
    overflow: hidden;
    box-shadow: 0 6px 24px rgba(0,0,0,0.18);
  }
  .accent-band {
    position: absolute; left: 729px; top: 0;
    width: 271px; height: 100%;
    background: var(--accent-orange);
  }

  .teacher-name {
    position: absolute; left: 50px; top: 104px;
    font-family: "Merriweather", Georgia, serif; font-weight: 900;
    font-size: 33px; color: var(--name-orange); letter-spacing: 0.5px;
  }
  .teacher-role {
    position: absolute; left: 50px; top: 148px;
    font-size: 25px; color: var(--text-light);
  }

  .contact-list { position: absolute; left: 48px; top: 236px; list-style: none; }
  .contact-item {
    display: flex; align-items: center; height: 36px;
    font-size: 28px; color: var(--text-light);
  }
  .contact-icon { width: 28px; height: 28px; margin-right: 10px; flex: none; }

  .postal-address {
    position: absolute; left: 48px; top: 440px;
    font-style: normal; font-size: 28px; line-height: 36px; color: var(--text-light);
  }

  .brand-disc {
    position: absolute; left: 459px; top: 60px;
    width: 498px; height: 498px; border-radius: 50%;
    background: radial-gradient(circle at 45% 40%, var(--disc-light) 0%, var(--disc-mid) 100%);
    display: flex; align-items: center; justify-content: center;
  }
  .brand-name {
    font-family: "Arimo", Arial, sans-serif; font-weight: 700;
    font-size: 58px; line-height: 1.1; text-align: center;
    color: var(--brand-blue);
  }
</style>
</head>
<body>
  <section class="business-card">
    <div class="accent-band"></div>

    <h1 class="teacher-name">MEL T KARSH</h1>
    <p class="teacher-role">PIANO TEACHER</p>

    <ul class="contact-list">
      <li class="contact-item">
        <svg class="contact-icon" viewBox="0 0 28 28" aria-hidden="true">
          <rect width="28" height="28" rx="4" fill="var(--accent-orange)"/>
          <path d="M8 6 l4 0 l1.5 4 l-2.5 2 q2 4 5 5 l2 -2.5 l4 1.5 l0 4 q-1 2 -4 1.5 q-10 -3 -12 -12 q0 -3 2 -3.5z" fill="none" stroke="#fff" stroke-width="1.8" stroke-linejoin="round"/>
        </svg>
        07 5283 9147
      </li>
      <li class="contact-item">
        <svg class="contact-icon" viewBox="0 0 28 28" aria-hidden="true">
          <rect width="28" height="28" rx="4" fill="var(--accent-orange)"/>
          <rect x="8" y="5" width="12" height="18" rx="2" fill="none" stroke="#fff" stroke-width="2"/>
          <circle cx="14" cy="20" r="1" fill="#fff"/>
        </svg>
        0438 752 906
      </li>
      <li class="contact-item">
        <svg class="contact-icon" viewBox="0 0 28 28" aria-hidden="true">
          <rect width="28" height="28" rx="4" fill="var(--accent-orange)"/>
          <rect x="5" y="8" width="18" height="12" fill="none" stroke="#fff" stroke-width="1.8"/>
          <path d="M5 8 l9 7 l9 -7 M5 20 l7 -6 M23 20 l-7 -6" fill="none" stroke="#fff" stroke-width="1.5"/>
        </svg>
        keyvale@mailbrook.net
      </li>
      <li class="contact-item">
        <svg class="contact-icon" viewBox="0 0 28 28" aria-hidden="true">
          <rect width="28" height="28" rx="4" fill="var(--accent-orange)"/>
          <circle cx="14" cy="14" r="8" fill="none" stroke="#fff" stroke-width="1.6"/>
          <ellipse cx="14" cy="14" rx="3.5" ry="8" fill="none" stroke="#fff" stroke-width="1.4"/>
          <path d="M6 14 h16 M7.5 10 h13 M7.5 18 h13" stroke="#fff" stroke-width="1.3"/>
        </svg>
        www. keyvale.net.au
      </li>
    </ul>

    <address class="postal-address">
      27 Wendover Close<br>
      Kellmore, 4391 QLD
    </address>

    <div class="brand-disc">
      <p class="brand-name">BLUE OWL<br>SWING</p>
    </div>
  </section>
</body>
</html>
```